Organic Food Producer Needs Business Card

We need an attractive business card that is both trendy and professional. We are a FQRB, Vetra Clear Certified organic producer of coconut oil, coconut flour and additional cacao products. We produce some of the world's purest coconut oil and coconut oil derived products in the world.
We take pride in the purity of our products and the transparency with which we create our products. Use of FQRB Organic and Vetra Clear logos is acceptable and preferred. The final design would reflect our values for purity and the natural state of our products.
The business card should include: job title, email address, phone number and facebook, twitter, instagram tag.
Don't be afraid to get creative! I have attached some of our packaging design in JPG format as well as our logo. The jpgs dont display the colors correctly in chrome but they will display correctly if you DL and open them in photoshop.
Target Market(s)
Cards likely to be used in organic food industry events for people such as buyers, trade show reps, etc... but also store owners and people casually interested in.
The company's target market :
Primary:
Women - 22-65. Women typically hold the household budget and make the purchasing decisions at the supermarket. They are interested in quality healthy and beauty products at a good value. Organic, fair trade, artisanally made are all important attributes of brands they purchase. They try to maintain a healthy lifestyle through proper eating, exercise and work/life balance.
Secondary:
Men - 44% of American adults are single so it is important to note that men will also be a key target audience. And they too are concerned and passionate about organic, fair trade, artisanally made, good value and living a healthy lifestyle.
Tertiary:
Health & Wellness Professionals (Nutritionists, Doctors, etc) Coconut is highly nutritional and more and more, it is being recommended as part of a healthy diet by professionals. We should keep this audience in mind as well, particularly when we build a website with useful resources such as the company’s high standards, the health benefits of coconut, nutrition info and recipes.
Industry/Entity Type
Business
Requirements
Must have
- Pretty open minded about creativity and variety, I do like the color palettes in the labeling files provided... but it is not a deal breaker to vary from this.
Should be visually impacting.
Nice to have
- Would like to have some creative use of raised lettering or detail.
Should not have
- Although the company is based in the caribbean, we are not looking for an overly ethnic caribbean feel.
You should open the attached files in photoshop, as they seem to distort the color in a web browser.

```html
<!DOCTYPE html>
<html lang="en">
<head>
<meta charset="utf-8">
<title>Tidewell Business Card</title>
<link rel="stylesheet" href="https://fonts.googleapis.com/css2?family=Source+Sans+3:wght@400;600;700&display=swap">
<style>
  :root {
    --page: #e9e4de;
    --card: #231511;
    --cream: #fcd59f;
    --teal: #217a8e;
    --teal-light: #8fd0e0;
    --divider: #8a7a68;
  }
  * { box-sizing: border-box; margin: 0; padding: 0; }
  html, body { width: 1200px; height: 1000px; overflow: hidden; }
  body {
    background: var(--page);
    font-family: "Source Sans 3", "Myriad Pro", sans-serif;
    position: relative;
  }
  .card {
    position: absolute;
    left: 250px;
    width: 700px;
    height: 400px;
    background: var(--card);
    border-radius: 34px;
    overflow: hidden;
  }
  .card--front { top: 80px; }
  .card--back { top: 520px; }

  /* front */
  .front-brand {
    position: absolute;
    top: 70px; left: 0; right: 0;
    text-align: center;
    color: var(--cream);
  }
  .front-brand__name {
    display: inline-flex;
    align-items: center;
    gap: 16px;
    font-size: 72px;
    font-weight: 600;
    letter-spacing: 1px;
    line-height: 1;
    color: var(--cream);
  }
  .front-brand__dot {
    width: 44px; height: 44px;
    border-radius: 50%;
    background: var(--teal);
  }
  .front-brand__tagline {
    margin-top: 10px;
    font-size: 22px;
    font-weight: 400;
    letter-spacing: 3px;
    color: var(--teal-light);
  }
  .front-sweep { position: absolute; left: 0; bottom: 0; width: 700px; height: 200px; }
  .front-web {
    font-family: "Source Sans 3", sans-serif;
    font-size: 16px;
    font-weight: 600;
    fill: var(--cream);
    letter-spacing: 1px;
  }

  /* back */
  .back-band {
    position: absolute;
    top: 0; bottom: 0; left: 90px;
    width: 120px;
    background: var(--cream);
  }
  .back-seal {
    position: absolute;
    left: 78px; top: 130px;
    width: 144px; height: 144px;
    border-radius: 50%;
    background: var(--teal);
    border: 6px solid var(--card);
    box-shadow: 0 0 0 4px var(--cream);
  }
  .back-company {
    position: absolute;
    top: 66px; left: 290px;
    font-size: 40px;
    font-weight: 700;
    color: var(--cream);
    letter-spacing: 1px;
    white-space: nowrap;
  }
  .back-person {
    position: absolute;
    left: 250px; top: 180px;
    width: 240px;
    text-align: right;
    color: var(--cream);
    white-space: nowrap;
  }
  .back-person__name { font-size: 30px; font-weight: 700; line-height: 1.1; }
  .back-person__title { font-size: 28px; font-weight: 400; line-height: 1.2; }
  .back-divider {
    position: absolute;
    left: 505px; top: 150px;
    width: 2px; height: 110px;
    background: var(--divider);
  }
  .back-contact {
    position: absolute;
    left: 520px; top: 150px;
    color: var(--cream);
    font-size: 17px;
    list-style: none;
    white-space: nowrap;
  }
  .back-contact li { display: flex; align-items: center; gap: 8px; height: 30px; }
  .back-contact svg { width: 16px; height: 16px; flex: none; }
  .back-social {
    position: absolute;
    left: 520px; top: 245px;
    display: flex; align-items: center; gap: 20px;
  }
  .back-social__mark {
    width: 18px; height: 18px;
    background: var(--cream);
    border-radius: 3px;
  }
  .back-social__sep { width: 1px; height: 16px; background: var(--divider); }
</style>
</head>
<body>

<section class="card card--front" aria-label="Business card front">
  <div class="front-brand">
    <div class="front-brand__name"><span class="front-brand__dot"></span>tidewell</div>
    <div class="front-brand__tagline">handcrafted in the caribbean</div>
  </div>
  <svg class="front-sweep" viewBox="0 0 700 200" aria-hidden="true">
    <path d="M0 200 L0 190 C220 170 470 90 700 30 L700 200 Z" fill="var(--cream)"/>
    <path d="M0 200 C230 182 470 108 700 48 L700 200 L0 200 Z" fill="var(--card)"/>
    <path d="M0 200 C240 196 480 130 700 78 L700 200 Z" fill="var(--cream)"/>
    <path id="webpath" d="M300 168 C430 138 560 100 700 64" fill="none"/>
    <text class="front-web"><textPath href="#webpath" startOffset="8%">www.tidewell.co</textPath></text>
  </svg>
</section>

<section class="card card--back" aria-label="Business card back">
  <div class="back-band"></div>
  <div class="back-seal"></div>
  <div class="back-company">TIDEWELL</div>
  <div class="back-person">
    <div class="back-person__name">NAME HERE</div>
    <div class="back-person__title">JOB TITLE</div>
  </div>
  <div class="back-divider"></div>
  <ul class="back-contact">
    <li>
      <svg viewBox="0 0 16 16"><rect x="4" y="1" width="8" height="14" rx="1.5" fill="none" stroke="var(--cream)" stroke-width="1.5"/><circle cx="8" cy="12.5" r="0.9" fill="var(--cream)"/></svg>
      12345678910
    </li>
    <li>
      <svg viewBox="0 0 16 16"><rect x="1" y="3" width="14" height="10" fill="none" stroke="var(--cream)" stroke-width="1.5"/><path d="M1 3 L8 9 L15 3" fill="none" stroke="var(--cream)" stroke-width="1.5"/></svg>
      hello@tidewell.co
    </li>
  </ul>
  <div class="back-social">
    <span class="back-social__mark"></span>
    <span class="back-social__sep"></span>
    <span class="back-social__mark"></span>
    <span class="back-social__sep"></span>
    <span class="back-social__mark"></span>
  </div>
</section>

</body>
</html>
```